Northern Guild of Acute Care Doctors Membership Poster Design

We need a poster that highlights why physicians should become a member of our association.

As the national voice of emergency medicine (EM), NGAD provides continuing medical education, advocates on behalf of emergency physicians and their patients, supports research and strengthens the EM community. In co-operation with other specialties and committees, NGAD also plays a vital role in the development of national standards and clinical guidelines.

NGAD keeps Canadian emergency physicians informed of developments in the clinical practice of EM and addresses political and societal changes, that affect the delivery of emergency health care.

Vision
Leading excellence in Emergency Medicine across Canada

Mission
NGAD champions excellence in Emergency Medicine in Canada by:

Advocating for Emergency Physicians and their patients;
Connecting Emergency Physicians;
Leading Emergency Medicine education;
Fostering research and innovation
Defining standards for quality Emergency Care
Collaborating with Emergency Care providers.

Target Market(s)

Physicians, Residents and Medical Students

Industry/Entity Type

Doctor

Font styles to use
Sans Serif

Requirements
Must have
• Why belong?
• Career Development
• Vision
• Leading excellence in Emergency Medicine across Canada
• Mission
• NGAD champions excellence in Emergency Medicine in Canada by:
• Advocating for Emergency Physicians and their patients;
• Connecting Emergency Physicians;
• Leading Emergency Medicine education;
• Fostering research and innovation
• Defining standards for quality Emergency Care
• Collaborating with Emergency Care providers.
• Financial Discounts
• Special rates at Larchwood Inns
• Discount on fares from Trellis Lines
• Discounts on home and auto insurance thought the Hearthbond Mutual and Brightvale Cover
• Special rates on medical and dental insurance through Maplecrest Benefits
• Special rates with Pellam Mobile or Vexor
• Discounts on tickets from Dunholt Stageworks
• Discounts on tickets from Footlights on Tour
• Advocacy
• NGAD advocates on behalf of you and your patients
• We support the development of the specialty of emergency medicine for you
• Gain a larger voice representing you and your specialty
• Networking Opportunities
• Opportunity to become involved with NGAD committees and sections
• Connect with colleagues and potential mentors at events and through online discussions
• Member Types
• Physician Members
• Resident Members
• Student Members
• Associate Members
• ngad-example.ca
• Corporate colours or colours that are complimentary to our corporate colours
• Hex 0077b2
• Hex DF0631
Nice to have
• Pictures

```html
<!DOCTYPE html>
<html lang="en">
<head>
<meta charset="utf-8">
<title>NGAD Membership Poster</title>
<link href="https://fonts.googleapis.com/css2?family=Josefin+Sans:wght@700&family=Catamaran:wght@500;600&display=swap" rel="stylesheet">
<style>
:root{
  --ngad-blue:#0077b2;
  --ngad-text-blue:#1565a8;
  --ngad-red:#df0631;
  --ngad-red-box:#d42030;
  --paper:#ffffff;
  --stage:#e9eaec;
}
html,body{margin:0;padding:0;width:806px;height:1200px;overflow:hidden;background:var(--stage);}
.poster{
  position:absolute;left:78px;top:0;width:697px;height:1289px;
  transform:scale(0.93096);transform-origin:top left;
  background:var(--paper);overflow:hidden;
  font-family:"Catamaran",sans-serif;font-weight:500;
}
.header-waves{position:absolute;left:0;top:0;width:697px;height:360px;}
.headline{
  position:absolute;left:0;top:34px;width:697px;margin:0;text-align:center;
  font-family:"Josefin Sans",sans-serif;font-weight:700;font-size:33px;line-height:37px;
  color:var(--paper);
}
.info{position:absolute;left:70px;top:334px;width:560px;}
.info h2{margin:0;font-size:25px;line-height:30px;font-weight:600;color:var(--ngad-red);}
.info p{margin:0 0 8px;font-size:17px;line-height:21.5px;color:var(--ngad-text-blue);}
.brand{
  position:absolute;left:440px;top:380px;width:190px;
  display:flex;align-items:center;justify-content:center;gap:12px;
}
.brand-dot{width:34px;height:34px;border-radius:50%;background:var(--ngad-blue);}
.brand-name{font-size:42px;font-weight:600;color:var(--ngad-blue);line-height:1;}
.benefits{
  position:absolute;left:42px;top:601px;width:613px;height:480px;
  background:var(--ngad-red-box);border-radius:30px;
}
.benefits ul{margin:0;padding:0 20px 0 85px;position:relative;top:15px;list-style:disc;}
.benefits li{color:var(--paper);font-size:17px;line-height:21.3px;padding-left:4px;}
.connect{
  position:absolute;left:70px;top:1084px;width:600px;margin:0;
  font-size:25px;line-height:28px;font-weight:600;color:var(--ngad-red);
}
.member-types{position:absolute;left:55px;top:1146px;margin:0;padding:0 0 0 42px;}
.member-types li{color:var(--ngad-red);font-size:17px;line-height:21.3px;}
.member-types span{color:var(--ngad-text-blue);}
.site-tab{
  position:absolute;left:390px;top:1178px;width:307px;height:75px;
  background:var(--ngad-red);border-top-left-radius:60px;
  display:flex;align-items:center;justify-content:center;
  color:var(--paper);font-size:28px;font-weight:600;
}
</style>
</head>
<body>
<div class="poster">
  <svg class="header-waves" viewBox="0 0 697 360" aria-hidden="true">
    <defs>
      <linearGradient id="mist" x1="0" y1="0" x2="0" y2="1">
        <stop offset="0.6" stop-color="#cfd2d6"/>
        <stop offset="1" stop-color="#ffffff"/>
      </linearGradient>
    </defs>
    <rect width="697" height="360" fill="url(#mist)"/>
    <path d="M0,210 C90,250 200,310 330,323 C420,330 560,305 697,235 V290 C560,328 420,340 330,337 C200,328 90,285 0,258Z" fill="var(--ngad-blue)"/>
    <path d="M0,185 C90,220 200,275 330,290 C420,300 560,280 697,205 V238 C560,305 420,328 330,320 C200,308 90,248 0,212Z" fill="var(--ngad-red)"/>
    <path d="M0,0 H697 V205 C560,280 420,300 330,290 C200,275 90,220 0,185Z" fill="var(--ngad-blue)" stroke="#ffffff" stroke-width="3"/>
  </svg>
  <h1 class="headline">NGAD keeps Canadian emergency<br>physicians informed of developments<br>in the clinical practice of EM and<br>addresses political and societal<br>changes, that affect the delivery of<br>emergency health care.</h1>

  <div class="info">
    <h2>Why belong?</h2>
    <p>Career Development</p>
    <h2>Vision</h2>
    <p>Leading excellence in Emergency<br>Medicine across Canada</p>
    <h2>Mission</h2>
    <p>NGAD champions excellence in Emergency Medicine in Canada by<br>Advocating for Emergency Physicians and their patients<br>Connecting Emergency Physicians<br>Leading Emergency Medicine education</p>
  </div>

  <div class="brand">
    <span class="brand-dot"></span>
    <span class="brand-name">NGAD</span>
  </div>

  <div class="benefits">
    <ul>
      <li>Fostering research and innovation</li>
      <li>Defining standards for quality Emergency Care</li>
      <li>Collaborating with Emergency Care providers.</li>
      <li>Financial Discounts</li>
      <li>Special rates at Larchwood Inns</li>
      <li>Discount on fares from Trellis Lines</li>
      <li>Discounts on home and auto insurance thought the</li>
      <li>Hearthbond Mutual and Brightvale Cover</li>
      <li>Special rates on medical and dental insurance through</li>
      <li>Maplecrest Benefits</li>
      <li>Special rates with Pellam Mobile or Vexor</li>
      <li>Discounts on tickets from Dunholt Stageworks</li>
      <li>Discounts on tickets from Footlights on Tour</li>
      <li>Advocacy</li>
      <li>NGAD advocates on behalf of you and your patients</li>
      <li>We support the development of the specialty of emergency medicine for you</li>
      <li>Gain a larger voice representing you and your specialty</li>
      <li>Networking Opportunities</li>
      <li>Opportunity to become involved with NGAD committees and sections</li>
    </ul>
  </div>

  <h2 class="connect">Connect with colleagues and potential mentors<br>at events and through online discussions</h2>
  <ul class="member-types">
    <li><span>Member Types</span></li>
    <li><span>Physician Members</span></li>
    <li><span>Resident Members</span></li>
    <li><span>Student Members</span></li>
    <li><span>Associate Members</span></li>
  </ul>

  <div class="site-tab">ngad-example.ca</div>
</div>
</body>
</html>
```